Stationary Design Letterhead and Envelope

Artist should provide Letterhead and envelop stationary designs

Info for stationary:
Fernhallow Outdoor Advertising
4873 Quarry Rd. 915 N. PO BOX 528617
Austin, TX 78519

Dale Fernhallow
President
555-862-1907
dale@fernhallowsigns.example
fernhallowsigns.example

Target Market(s)

clients

Colors
0054AA
0677BA
7BADD7
CADEEF
E8F1F8

Requirements
Must have
• high quality unique eye catching and dynamic

```html
<!DOCTYPE html>
<html lang="en">
<head>
<meta charset="utf-8">
<title>Fernhallow Outdoor Advertising – Stationery</title>
<link href="https://fonts.googleapis.com/css2?family=Montserrat:wght@600;700&family=Roboto:wght@300;400;500&display=swap" rel="stylesheet">
<style>
  :root{
    --blue:#0677BA;
    --blue-deep:#0054AA;
    --blue-soft:#7BADD7;
    --blue-pale:#CADEEF;
    --ink:#111111;
    --text:#3a3a3a;
    --paper:#ffffff;
    --paper-tint:#f6f6f6;
    --backdrop:#d8cbb3;
  }
  *{margin:0;padding:0;box-sizing:border-box}
  html,body{width:1200px;height:783px;overflow:hidden}
  body{background:var(--backdrop);font-family:"Roboto",sans-serif;color:var(--text);position:relative}

  .sheet{position:absolute;background:var(--paper);box-shadow:0 6px 20px rgba(0,0,0,.18);overflow:hidden}
  .sheet svg.deco{position:absolute;left:0;top:0}

  .brand{position:absolute;display:flex;align-items:center;gap:8px}
  .brand-mark{width:12px;height:12px;background:var(--blue-deep);flex:none}
  .brand-name{font-family:"Montserrat",sans-serif;font-weight:700;color:var(--blue-deep);letter-spacing:.5px;white-space:nowrap;text-transform:uppercase;line-height:1.15}

  /* Letterhead */
  .letterhead{left:30px;top:30px;width:520px;height:723px}
  .letterhead .brand{left:34px;top:55px}
  .letterhead .brand-name{font-size:11px}
  .letterhead .date{position:absolute;right:40px;top:150px;font-size:8px;color:#555}
  .sender{position:absolute;left:60px;top:190px;font-size:8px;line-height:1.55}
  .sender-name{font-size:12px;font-weight:500;color:var(--ink)}
  .sender-name span{color:var(--blue)}
  .sender-role{margin-bottom:3px}
  .sender .tag{color:var(--blue);font-weight:500}
  .letter-body{position:absolute;left:60px;right:50px;top:300px;font-size:9px;font-weight:300;line-height:1.75;color:#444}
  .letter-body p{margin-bottom:14px}

  .contact-list{position:absolute;list-style:none;font-size:8px;line-height:1.2}
  .contact-list li{display:flex;align-items:center;gap:6px;margin-bottom:3px}
  .contact-list svg{flex:none}
  .letterhead .contact-list{left:60px;bottom:78px}

  /* Envelope */
  .envelope{width:580px;height:252px;left:590px}
  .envelope-front{top:60px;background:var(--paper-tint)}
  .envelope-front .brand{left:46px;top:33px}
  .envelope-front .brand-name{font-size:11px}
  .envelope-front .contact-list{left:46px;top:178px;font-size:7.5px}
  .envelope-back{top:380px}
  .envelope-back .brand{right:24px;bottom:18px}
  .envelope-back .brand-mark{width:9px;height:9px}
  .envelope-back .brand-name{font-size:8px;line-height:1.2}
</style>
</head>
<body>

<!-- Letterhead -->
<section class="sheet letterhead" aria-label="Letterhead">
  <svg class="deco" width="520" height="723" viewBox="0 0 520 723" aria-hidden="true">
    <!-- header: stepped blocks and diagonal stripes -->
    <rect x="0" y="0" width="520" height="6" fill="var(--blue-deep)"/>
    <rect x="0" y="96" width="300" height="2" fill="var(--blue-pale)"/>
    <polygon points="300,6 520,6 520,110 400,110" fill="var(--blue)"/>
    <polygon points="360,6 420,6 520,90 520,110 500,110" fill="var(--ink)"/>
    <polygon points="440,6 470,6 520,46 520,70" fill="var(--blue-soft)"/>
    <!-- footer: plain bands -->
    <rect x="0" y="700" width="520" height="10" fill="var(--blue)"/>
    <rect x="0" y="712" width="520" height="3" fill="var(--ink)"/>
    <rect x="380" y="690" width="140" height="10" fill="var(--blue-deep)"/>
  </svg>

  <div class="brand"><span class="brand-mark"></span><div class="brand-name">Fernhallow<br>Outdoor Advertising</div></div>
  <div class="date">Date : 13 April, 2023</div>

  <div class="sender">
    <div class="sender-name">Dale <span>Fernhallow</span></div>
    <div class="sender-role">President</div>
    <div><span class="tag">A :</span> PO BOX 528617 &nbsp;Austin, TX 78519</div>
    <div><span class="tag">W :</span> fernhallowsigns.example</div>
    <div><span class="tag">P :</span> +555 862 1907</div>
  </div>

  <div class="letter-body">
    <p>Lorem ipsum dolor sit amet, consectetur adipisicing elit, sed do eiusmod tempor incididunt ut labore et dolore magna aliqua. Ut enim ad minim veniam, quis nostrud exercitation ullamco laboris nisi ut aliquip ex ea commodo consequat.</p>
    <p>Excepteur sint occaecat cupidatat non proident, sunt in culpa qui officia deserunt mollit anim id est laborum. Sed ut perspiciatis unde omnis iste natus error sit voluptatem accusantium doloremque laudantium, totam rem aperiam, eaque ipsa quae ab illo inventore veritatis et quasi architecto beatae vitae dicta sunt explicabo. Nemo enim ipsam voluptatem quia voluptas sit aspernatur aut odit aut fugit, sed quia voluptatem sequi nesciunt.</p>
    <p>Neque porro quisquam dolorem ipsum quia dolor sit amet, consectetur, adipisci velit, sed quia non numquam magnam aliquam quaerat voluptatem. Sunt in culpa qui officia iste natus error sit voluptatem laudantium.</p>
  </div>

  <ul class="contact-list">
    <li><svg width="9" height="9" viewBox="0 0 10 10"><circle cx="5" cy="5" r="5" fill="var(--blue)"/><rect x="3.8" y="2.5" width="2.4" height="5" rx=".6" fill="#fff"/></svg>+ 555 862 1907</li>
    <li><svg width="9" height="9" viewBox="0 0 10 10"><circle cx="5" cy="5" r="5" fill="var(--blue)"/><circle cx="5" cy="5" r="2.4" fill="none" stroke="#fff" stroke-width="1"/></svg>fernhallowsigns.example</li>
    <li><svg width="9" height="9" viewBox="0 0 10 10"><circle cx="5" cy="5" r="5" fill="var(--blue)"/><rect x="2.6" y="3.4" width="4.8" height="3.2" fill="#fff"/></svg>dale@fernhallowsigns.example</li>
    <li><svg width="9" height="9" viewBox="0 0 10 10"><circle cx="5" cy="5" r="5" fill="var(--blue)"/><path d="M5 2.3a1.8 1.8 0 0 1 1.8 1.8C6.8 5.4 5 7.7 5 7.7S3.2 5.4 3.2 4.1A1.8 1.8 0 0 1 5 2.3z" fill="#fff"/></svg>4873 Quarry Rd. 915 N. PO BOX 528617 Austin, TX 78519.</li>
  </ul>
</section>

<!-- Envelope front -->
<section class="sheet envelope envelope-front" aria-label="Envelope front">
  <svg class="deco" width="580" height="252" viewBox="0 0 580 252" aria-hidden="true">
    <rect x="0" y="0" width="580" height="5" fill="var(--blue-deep)"/>
    <rect x="0" y="76" width="340" height="2" fill="var(--blue-pale)"/>
    <polygon points="340,5 580,5 580,100 450,100" fill="var(--blue)"/>
    <polygon points="400,5 460,5 580,80 580,100 560,100" fill="var(--ink)"/>
    <polygon points="500,5 530,5 580,38 580,60" fill="var(--blue-soft)"/>
  </svg>
  <div class="brand"><span class="brand-mark"></span><div class="brand-name">Fernhallow<br>Outdoor Advertising</div></div>
  <ul class="contact-list">
    <li><svg width="8" height="8" viewBox="0 0 10 10"><circle cx="5" cy="5" r="5" fill="var(--blue)"/><rect x="3.8" y="2.5" width="2.4" height="5" rx=".6" fill="#fff"/></svg>+ 555 862 1907</li>
    <li><svg width="8" height="8" viewBox="0 0 10 10"><circle cx="5" cy="5" r="5" fill="var(--blue)"/><circle cx="5" cy="5" r="2.4" fill="none" stroke="#fff" stroke-width="1"/></svg>fernhallowsigns.example</li>
    <li><svg width="8" height="8" viewBox="0 0 10 10"><circle cx="5" cy="5" r="5" fill="var(--blue)"/><rect x="2.6" y="3.4" width="4.8" height="3.2" fill="#fff"/></svg>dale@fernhallowsigns.example</li>
    <li><svg width="8" height="8" viewBox="0 0 10 10"><circle cx="5" cy="5" r="5" fill="var(--blue)"/><path d="M5 2.3a1.8 1.8 0 0 1 1.8 1.8C6.8 5.4 5 7.7 5 7.7S3.2 5.4 3.2 4.1A1.8 1.8 0 0 1 5 2.3z" fill="#fff"/></svg>4873 Quarry Rd. 915 N. PO BOX 528617 Austin, TX 78519.</li>
  </ul>
</section>

<!-- Envelope back -->
<section class="sheet envelope envelope-back" aria-label="Envelope back">
  <svg class="deco" width="580" height="252" viewBox="0 0 580 252" aria-hidden="true">
    <path d="M10 0 H580 L560 72 Q552 102 522 102 H58 Q32 102 24 72 Z" fill="var(--blue)"/>
  </svg>
  <div class="brand"><span class="brand-mark"></span><div class="brand-name">Fernhallow<br>Outdoor Advertising</div></div>
</section>

</body>
</html>
```